Business Card Design for Quorvane

Need a business card designed for Quorvane employees.
- 2 sided business card
- Front:
Company Logo (file attached)
Background could be:white with perhaps a red/black stripe on the left
OR
Background could be: OR dark red-black gradient: be creative
Include the following on the front:
Martin Delacroy
Founder & CEO
martin.delacroy@quorvane-example.com
+1 555.013.4782
quorvane-example.com
- Back: White color background with company logo
Text under the logo: Invoice Automation 2.0
** be creative about the font, mix of upper and lower case and colors for the text **
Target Market(s)
We are a software company marketing our products to large and medium sized businesses.
Industry/Entity Type
Business

```html
<!DOCTYPE html>
<html lang="en">
<head>
<meta charset="utf-8">
<title>Quorvane Business Card</title>
<link href="https://fonts.googleapis.com/css2?family=Arimo:wght@400;700&display=swap" rel="stylesheet">
<style>
  :root {
    --page-bg: #ffffff;
    --card-bg: #ffffff;
    --card-border: #8a8a8a;
    --ink: #111111;
    --brand-ink: #2b2b2b;
    --mark-fill: #3a3a3a;
  }
  * { margin: 0; padding: 0; box-sizing: border-box; }
  html, body {
    width: 1005px;
    height: 1200px;
    overflow: hidden;
    background: var(--page-bg);
    font-family: "Arimo", Arial, sans-serif;
    color: var(--ink);
  }
  .sheet { position: relative; width: 1005px; height: 1200px; }
  .card {
    position: absolute;
    left: 52px;
    width: 901px;
    height: 515px;
    background: var(--card-bg);
    border: 1px solid var(--card-border);
    overflow: hidden;
  }
  .card--back { top: 68px; }
  .card--front { top: 616px; }
  .decor { position: absolute; inset: 0; width: 100%; height: 100%; }
  .brand-mark {
    position: absolute;
    border-radius: 50%;
    background: var(--mark-fill);
  }
  .brand-name {
    position: absolute;
    font-weight: 400;
    color: var(--brand-ink);
    letter-spacing: 1px;
    line-height: 1;
    white-space: nowrap;
  }
  .card--back .brand-mark { left: 150px; top: 176px; width: 140px; height: 140px; }
  .card--back .brand-name { left: 338px; top: 188px; font-size: 82px; }
  .tagline {
    position: absolute;
    left: 340px;
    top: 300px;
    font-size: 31px;
    line-height: 1;
  }
  .card--front .brand-mark { left: 60px; top: 70px; width: 92px; height: 92px; }
  .card--front .brand-name { left: 176px; top: 80px; font-size: 47px; }
  .contact { position: absolute; left: 49px; top: 228px; z-index: 2; }
  .contact__name { font-size: 32px; font-weight: 700; line-height: 1.1; }
  .contact__role { font-size: 26px; line-height: 1.25; margin-bottom: 32px; }
  .contact__line { font-size: 28px; line-height: 1.5; white-space: nowrap; }
</style>
</head>
<body>
<main class="sheet">
  <section class="card card--back" aria-label="Card back">
    <svg class="decor" viewBox="0 0 901 515" role="img" aria-label="Corner areas for the brand's patterned sphere decoration">
      <defs>
        <radialGradient id="cornerDark" cx="0.3" cy="0.3" r="0.8">
          <stop offset="0" stop-color="#111"/>
          <stop offset="1" stop-color="#555"/>
        </radialGradient>
        <radialGradient id="cornerWarm" cx="0.7" cy="0.7" r="0.8">
          <stop offset="0" stop-color="#c8601f"/>
          <stop offset="1" stop-color="#f0a060"/>
        </radialGradient>
      </defs>
      <circle cx="-10" cy="-30" r="175" fill="url(#cornerDark)" opacity="0.9"/>
      <circle cx="990" cy="600" r="210" fill="url(#cornerWarm)" opacity="0.9"/>
    </svg>
    <div class="brand-mark" aria-hidden="true"></div>
    <div class="brand-name">Quorvane</div>
    <p class="tagline">Invoice Automation 2.0</p>
  </section>

  <section class="card card--front" aria-label="Card front">
    <svg class="decor" viewBox="0 0 901 515" role="img" aria-label="Large area for the brand's patterned sphere decoration">
      <defs>
        <linearGradient id="sphereTone" x1="0" y1="0" x2="0" y2="1">
          <stop offset="0" stop-color="#9a9a9a"/>
          <stop offset="0.3" stop-color="#1a1a1a"/>
          <stop offset="0.55" stop-color="#3a3a3a"/>
          <stop offset="0.7" stop-color="#b8591f"/>
          <stop offset="1" stop-color="#f0a060"/>
        </linearGradient>
      </defs>
      <circle cx="935" cy="250" r="340" fill="url(#sphereTone)" opacity="0.85"/>
    </svg>
    <div class="brand-mark" aria-hidden="true"></div>
    <div class="brand-name">Quorvane</div>
    <div class="contact">
      <p class="contact__name">Martin Delacroy</p>
      <p class="contact__role">Founder &amp; CEO</p>
      <p class="contact__line">martin.delacroy@quorvane-example.com</p>
      <p class="contact__line">+1 555.013.4782</p>
      <p class="contact__line">quorvane-example.com</p>
    </div>
  </section>
</main>
</body>
</html>
```